Security Camera Sign

14” high x 11” wide Color: Blue, Yellow, Black and white

Make the sign vertical
Replace red with blue
WARNING: Black over yellow
These premises are protected by Closed Circuit Television: On white
Images are recorded for crime prevention and public safety. Unauthorized access, theft or vandalism will result in prosecution: On Blue

Target Market(s)

Outdoor commercial building

Industry/Entity Type

Security

Requirements
Nice to have
• I would like the sign stand out. If you need more colors? Thanks Ok

```html
<!DOCTYPE html>
<html lang="en">
<head>
<meta charset="utf-8">
<title>Security Camera Sign</title>
<link rel="stylesheet" href="https://fonts.googleapis.com/css2?family=Anton&family=Bebas+Neue&display=swap">
<style>
  :root {
    --sign-blue: #002a86;
    --sign-yellow: #ffd300;
    --ink: #1f1414;
    --paper: #ffffff;
    --charcoal: #2d2d2d;
    --panel-grey: #dedede;
    --art-light: #eef0f4;
    --art-mid: #c9cfdc;
  }
  * { box-sizing: border-box; margin: 0; padding: 0; }
  html, body { width: 1000px; height: 1200px; overflow: hidden; background: var(--paper); }
  .canvas { position: relative; width: 1000px; height: 1200px; background: var(--paper); }
  .block { position: absolute; }

  /* Compact preview of the sign */
  .mini-header { left: 331px; top: 55px; width: 337px; height: 56px; background: var(--charcoal); }
  .mini-title {
    left: 361px; top: 60px; width: 279px; height: 46px; background: var(--panel-grey);
    display: flex; align-items: center; justify-content: center;
    font-family: "Anton", sans-serif; font-size: 40px; letter-spacing: 7px; color: var(--ink); line-height: 1;
  }
  .mini-camera { left: 337px; top: 125px; width: 162px; height: 116px; }
  .mini-message {
    left: 500px; top: 133px; width: 162px; text-align: center;
    font-family: "Bebas Neue", sans-serif; font-size: 21px; line-height: 25px; color: var(--ink);
  }
  .mini-footer {
    left: 331px; top: 253px; width: 337px; height: 67px; background: var(--charcoal);
    display: flex; flex-direction: column; align-items: center; justify-content: center;
    font-family: "Bebas Neue", sans-serif; font-size: 10px; line-height: 14px; color: var(--paper); text-align: center;
  }

  /* Full sign */
  .warning-band { left: 34px; top: 366px; width: 931px; height: 155px; background: var(--sign-blue); }
  .warning-label {
    left: 115px; top: 375px; width: 770px; height: 136px; background: var(--sign-yellow);
    display: flex; align-items: center; justify-content: center;
    font-family: "Anton", sans-serif; font-size: 132px; letter-spacing: 34px; padding-left: 34px;
    color: var(--ink); line-height: 1;
  }
  .camera-art { left: 50px; top: 565px; width: 452px; height: 285px; }
  .cctv-message {
    left: 505px; top: 578px; width: 450px; text-align: center;
    font-family: "Bebas Neue", sans-serif; font-size: 62px; line-height: 70px; letter-spacing: 1px; color: var(--ink);
  }
  .notice-band {
    left: 34px; top: 912px; width: 931px; height: 186px; background: var(--sign-blue);
    display: flex; flex-direction: column; align-items: center; justify-content: center;
    padding-bottom: 38px;
    font-family: "Bebas Neue", sans-serif; font-size: 31px; line-height: 36px; letter-spacing: 0.5px;
    color: var(--paper); text-align: center;
  }
</style>
</head>
<body>
<main class="canvas">
  <section class="sign-preview">
    <div class="block mini-header"></div>
    <div class="block mini-title">WARNING</div>
    <svg class="block mini-camera" viewBox="0 0 162 116" role="img" aria-label="Illustration of a bullet-style CCTV camera on a wall mount">
      <defs>
        <linearGradient id="miniArt" x1="0" y1="0" x2="1" y2="1">
          <stop offset="0" stop-color="var(--art-light)"/>
          <stop offset="1" stop-color="#cfcfcf"/>
        </linearGradient>
      </defs>
      <rect width="162" height="116" fill="url(#miniArt)"/>
    </svg>
    <p class="block mini-message">These premises<br>are protected<br>by closed<br>circuit television</p>
    <div class="block mini-footer">
      <span>Images are recorded for crime prevention and public safety</span>
      <span>Unauthorized access, theft or vandalism will result in prosecution</span>
    </div>
  </section>

  <section class="sign-full">
    <div class="block warning-band"></div>
    <div class="block warning-label">WARNING</div>
    <svg class="block camera-art" viewBox="0 0 452 285" role="img" aria-label="Illustration of a bullet-style CCTV camera with infrared LED ring on a wall mount">
      <defs>
        <linearGradient id="cameraArt" x1="0" y1="0" x2="1" y2="1">
          <stop offset="0" stop-color="var(--art-light)"/>
          <stop offset="1" stop-color="var(--art-mid)"/>
        </linearGradient>
      </defs>
      <rect width="452" height="285" fill="url(#cameraArt)"/>
    </svg>
    <p class="block cctv-message">These premises<br>are protected<br>by closed<br>circuit television</p>
    <div class="block notice-band">
      <span>Images are recorded for crime prevention and public safety</span>
      <span>Unauthorized access, theft or vandalism will result in prosecution</span>
    </div>
  </section>
</main>
</body>
</html>
```